Business Card Design Project

Basic business card with minimal details. I just need company name, email & web address, telephone and my name.
I would like the back of the card to be grey with my logo & company name centred.

Target Market(s)

Architects
Builders
Property Developers

Industry/Entity Type

Business

Font styles to use
Sans Serif

Colors

Designer to choose colors to be used in the design.

Requirements
Must have
• Venture Frame
Marcus Hadley - Director
M: 0452 913084
E: marcus@ventureframe.com.au
W: www.ventureframe.com.au
Should not have
• No other images or pictures

```html
<!DOCTYPE html>
<html lang="en">
<head>
<meta charset="utf-8">
<title>Venture Frame – Business Card</title>
<link rel="stylesheet" href="https://fonts.googleapis.com/css2?family=Arimo:wght@400;700&display=swap">
<style>
  :root {
    --stage-light: #f3f3f3;
    --stage-dark: #d9d9d8;
    --card-grey-light: #c2c2c1;
    --card-grey-mid: #9d9c9a;
    --card-grey-dark: #7f7e7c;
    --accent-red: #c8322f;
    --name-grey: #7a7a7a;
    --title-grey: #8d8d8d;
    --white: #ffffff;
  }
  * { box-sizing: border-box; margin: 0; padding: 0; }
  html, body {
    width: 1200px;
    height: 999px;
    overflow: hidden;
  }
  body {
    position: relative;
    font-family: "Arimo", Arial, sans-serif;
    background: radial-gradient(ellipse at 50% 45%, var(--stage-light) 0%, var(--stage-dark) 80%);
  }

  /* Card back */
  .card-back {
    position: absolute;
    left: 262px;
    top: 87px;
    width: 689px;
    height: 393px;
    background: linear-gradient(110deg, var(--card-grey-light) 0%, var(--card-grey-mid) 45%, var(--card-grey-dark) 80%);
  }
  .brand {
    position: absolute;
    left: 30px;
    top: 176px;
    display: flex;
    align-items: center;
    gap: 34px;
  }
  .brand-mark {
    width: 58px;
    height: 58px;
    background: var(--accent-red);
  }
  .brand-name {
    font-family: "Arimo", Arial, sans-serif;
    font-weight: 400;
    font-size: 50px;
    letter-spacing: 3px;
    text-transform: uppercase;
    color: var(--white);
    white-space: nowrap;
  }

  /* Card front */
  .card-front {
    position: absolute;
    left: 263px;
    top: 526px;
    width: 690px;
    height: 396px;
    overflow: hidden;
  }
  .identity {
    height: 140px;
    background: var(--white);
    padding: 40px 0 0 30px;
  }
  .person-name {
    font-weight: 700;
    font-size: 30px;
    color: var(--name-grey);
    text-transform: uppercase;
    line-height: 1;
  }
  .person-role {
    margin-top: 6px;
    font-size: 21px;
    color: var(--title-grey);
    line-height: 1;
  }
  .contacts {
    height: 256px;
    background: linear-gradient(100deg, var(--card-grey-dark) 0%, var(--card-grey-mid) 55%, var(--card-grey-light) 100%);
    list-style: none;
    padding-top: 34px;
  }
  .contact {
    display: flex;
    align-items: center;
    height: 70px;
    padding-left: 28px;
    color: var(--white);
    font-size: 22px;
  }
  .contact svg {
    width: 32px;
    height: 30px;
    margin-right: 20px;
    flex: none;
  }
</style>
</head>
<body>
  <section class="card-back" aria-label="Card back">
    <div class="brand">
      <span class="brand-mark" aria-hidden="true"></span>
      <span class="brand-name">Venture Frame</span>
    </div>
  </section>

  <section class="card-front" aria-label="Card front">
    <header class="identity">
      <h1 class="person-name">Marcus Hadley</h1>
      <p class="person-role">Director</p>
    </header>
    <ul class="contacts">
      <li class="contact">
        <svg viewBox="0 0 32 30" aria-hidden="true">
          <rect x="7" y="1" width="14" height="27" rx="2" fill="none" stroke="var(--accent-red)" stroke-width="1.5"/>
          <line x1="7" y1="5" x2="21" y2="5" stroke="var(--accent-red)" stroke-width="1.2"/>
          <line x1="7" y1="22" x2="21" y2="22" stroke="var(--accent-red)" stroke-width="1.2"/>
          <circle cx="14" cy="25" r="1.2" fill="var(--accent-red)"/>
        </svg>
        <span>0452 913084</span>
      </li>
      <li class="contact">
        <svg viewBox="0 0 32 30" aria-hidden="true">
          <rect x="1" y="8" width="28" height="16" fill="none" stroke="var(--accent-red)" stroke-width="1.5"/>
          <polyline points="1,8 15,18 29,8" fill="none" stroke="var(--accent-red)" stroke-width="1.5"/>
        </svg>
        <span>marcus@ventureframe.com.au</span>
      </li>
      <li class="contact">
        <svg viewBox="0 0 32 30" aria-hidden="true">
          <text x="0" y="12" font-family="Arimo, Arial, sans-serif" font-size="10" fill="var(--accent-red)">www</text>
          <path d="M22 10 L22 26 L25 23 L28 29 L30 28 L27 22 L31 22 Z" fill="var(--white)" stroke="var(--accent-red)" stroke-width="1"/>
        </svg>
        <span>www.ventureframe.com.au</span>
      </li>
    </ul>
  </section>
</body>
</html>
```